[AMAZING DESIGN NEEDED] Women's Fishing Squeeze Page

I need a professional design for a landing page that is going to collect email addresses.

You can use the creatives already on the page or you can pull images from the facebook/instagram pages.
https://www.facebook.com/LuresLinesLaces
https://www.instagram.com/lureslinesandlaces/

This is the page that needs designed: https://lureslinesandlaces-example.com/email-opt-in/

See attached for examples.

Target Market(s)

Women who like to go fishing

Industry/Entity Type

Fishing

Number of Pages Required

1 page

Font styles to use
Sans Serif

Requirements
Must have
• excellent design. Call to actions.

```html
<!DOCTYPE html>
<html lang="en">
<head>
<meta charset="utf-8">
<title>TideTackleCo – Email Opt-In</title>
<link href="https://fonts.googleapis.com/css2?family=Oswald:wght@300;400;500&family=Montserrat:wght@500&family=Roboto:wght@500&display=swap" rel="stylesheet">
<style>
  :root {
    --sand: #cdbba9;
    --ink: #3c3a36;
    --ocean: #00a6d0;
    --ocean-bright: #12bee3;
    --ocean-deep: #0a8fb8;
    --form-bg: #0c6a88;
    --aqua: #3fd3dd;
    --white: #ffffff;
    --field-text: #1a7f9c;
    --logo: #1a9aa8;
    --divider: #111111;
  }
  * { box-sizing: border-box; margin: 0; padding: 0; }
  html, body { width: 1200px; height: 356px; overflow: hidden; background: var(--white); }
  .canvas { position: relative; width: 1200px; height: 356px; display: flex; }
  .divider { width: 1px; height: 356px; background: var(--divider); flex: none; }
  .page { position: relative; width: 599.5px; height: 356px; overflow: hidden; flex: none; }

  .site-header { position: absolute; left: 0; top: 0; width: 100%; height: 98px; background: var(--sand); }
  .brand {
    position: absolute; left: 301px; top: 30px; transform: translateX(-50%);
    display: flex; align-items: center; gap: 4px; white-space: nowrap;
    font-family: "Oswald", sans-serif; font-weight: 400; font-size: 13px; color: var(--logo);
    letter-spacing: 0.3px;
  }
  .brand-dot { width: 7px; height: 7px; border-radius: 50%; background: var(--logo); }
  .main-nav {
    position: absolute; left: 174px; top: 86px;
    display: flex; gap: 12px; white-space: nowrap;
    font-family: "Roboto", sans-serif; font-weight: 500; font-size: 5.4px;
    color: var(--ink); text-transform: uppercase; letter-spacing: 0.1px;
  }
  .main-nav .has-menu::after { content: " \2304"; font-size: 5px; }

  .hero { position: absolute; left: 0; top: 98px; width: 100%; height: 258px; background: var(--ocean); }
  .hero--pattern { background: linear-gradient(180deg, var(--ocean-bright) 0%, var(--ocean-bright) 58%, var(--ocean-deep) 80%, var(--ocean-bright) 100%); }

  .model-photo {
    position: absolute; left: 138px; top: 5px; width: 156px; height: 253px;
    background: linear-gradient(180deg, #2b4a55 0%, #7a4a36 35%, #1d5e63 60%, #b5323a 100%);
    border-radius: 60px 60px 8px 8px;
    opacity: 0.85;
  }

  .signup {
    position: absolute; left: 323px; top: 45px; width: 127px; height: 169px;
    background: var(--form-bg); text-align: center; padding-top: 9px;
    font-family: "Oswald", sans-serif; text-transform: uppercase; color: var(--white);
    white-space: nowrap;
  }
  .signup-title { font-weight: 400; font-size: 17px; line-height: 19px; color: var(--aqua); }
  .signup-offer { font-weight: 300; font-size: 11.5px; line-height: 18px; }
  .signup-offer strong { font-weight: 400; font-size: 17px; }
  .signup-sub { font-weight: 300; font-size: 11.5px; line-height: 15px; }

  .signup-form { position: absolute; left: 8px; top: 73px; width: 111px; }
  .field, .subscribe {
    display: block; width: 111px; height: 18px; border-radius: 3px; border: 0;
    font-family: "Montserrat", sans-serif; font-weight: 500; text-transform: none;
  }
  .field {
    background: var(--white); color: var(--field-text);
    font-size: 7px; line-height: 18px; text-align: left; padding-left: 8px; margin-bottom: 4.3px;
  }
  .subscribe { background: var(--aqua); color: #0d2e38; font-size: 8px; line-height: 18px; text-align: center; }
  .subscribe--sand { background: var(--sand); }
</style>
</head>
<body>
<div class="canvas">

  <section class="page">
    <header class="site-header">
      <div class="brand"><span class="brand-dot"></span>TideTackleCo</div>
      <nav class="main-nav">
        <span class="has-menu">Clothing</span><span>Hats</span><span>Bundles</span>
        <span>Accessories &amp; Stickers</span><span>Jewelry</span><span>Clearance</span>
      </nav>
    </header>
    <main class="hero">
      <div class="model-photo" role="img" aria-label="Photo of a woman in a trucker cap, sunglasses and a teal graphic tee with a flannel tied at the waist"></div>
      <div class="signup">
        <p class="signup-title">Sign up today</p>
        <p class="signup-offer">And receive <strong>15% off</strong></p>
        <p class="signup-sub">Your next order</p>
        <div class="signup-form">
          <div class="field">First Name*</div>
          <div class="field">Last Name</div>
          <div class="field">Email*</div>
          <div class="subscribe">Subscribe Now</div>
        </div>
      </div>
    </main>
  </section>

  <div class="divider"></div>

  <section class="page">
    <header class="site-header">
      <div class="brand"><span class="brand-dot"></span>TideTackleCo</div>
      <nav class="main-nav">
        <span class="has-menu">Clothing</span><span>Hats</span><span>Bundles</span>
        <span>Accessories &amp; Stickers</span><span>Jewelry</span><span>Clearance</span>
      </nav>
    </header>
    <main class="hero hero--pattern" role="img" aria-label="Bright blue background with a faint illustrated fish pattern above layered water waves">
      <div class="model-photo" role="img" aria-label="Photo of a woman in a trucker cap, sunglasses and a teal graphic tee with a flannel tied at the waist"></div>
      <div class="signup">
        <p class="signup-title">Sign up today</p>
        <p class="signup-offer">And receive <strong>15% off</strong></p>
        <p class="signup-sub">Your next order</p>
        <div class="signup-form">
          <div class="field">First Name*</div>
          <div class="field">Last Name</div>
          <div class="field">Email*</div>
          <div class="subscribe subscribe--sand">Subscribe Now</div>
        </div>
      </div>
    </main>
  </section>

</div>
</body>
</html>
```